Online Cooking App Pitch Deck- (THIS IS NOT A FOOD BUSINESS OR FOOD SERVICE, NO FOOD PICTURES)

Project Goal:
Design a visually compelling pitch deck to be used for securing investment. Looking for the pitch deck to be about the design using shapes, colors, fonts and sizes. Must be creative yet simple and clean.
Color Palette:
https://palettrix.example/ff3800-ffe2db-fefefa-2d3e50-010b13

(We want most screens to use #FEFEFA)

This is the current pitch deck we need simplified and redesigned (USE TEXT IN THE GOOGLE LINK TO SHOW IN YOUR DESIGN):

https://slides.vornidex.example/deck/8QmTzR42kLpWx7nHa3Jv-cYdoeBtfGuqN/edit?share=link&uid=592031846720518390417&fmt=true&mode=true

Project is now guaranteed. Remember use the text in the google link in powerpoint design. Use a little more color not just the logo color. Do not use any pictures of food this is not food related business. We care more about style and design of shapes, text, color fonts.

Target Market(s)

Investors (venture capitalists, angel investors) interested in innovative technology solutions within the food industry.

Font styles to use
Serif
Sans Serif

Requirements
Nice to have
• Simple, abstract background non distracting but complementary.
Should not have
• No pictures

```html
<!DOCTYPE html>
<html lang="en">
<head>
<meta charset="utf-8">
<title>Ladle &amp; Lore — Investor Deck Overview</title>
<link href="https://fonts.googleapis.com/css2?family=Lato:wght@400;700;900&family=Roboto:wght@400;500;700&display=swap" rel="stylesheet">
<style>
  :root{
    --orange:#ff3800;
    --blush:#ffe2db;
    --cream:#fefefa;
    --slate:#2d3e50;
    --ink:#010b13;
    --blue:#0b6cc3;
    --blue-deep:#0d4f8f;
    --canvas:#f4f4f4;
    --text:#3a3a3a;
  }
  *{box-sizing:border-box;margin:0;padding:0}
  html,body{width:1026px;height:1200px;overflow:hidden;background:var(--canvas)}
  .board{position:relative;width:1026px;height:1200px}
  .slide{position:absolute;width:765px;height:430px;transform:scale(.5794);transform-origin:0 0;overflow:hidden;background:var(--cream);box-shadow:0 2px 8px rgba(0,0,0,.08);font-family:"Roboto",sans-serif;color:var(--text)}
  .col-l{left:51px}.col-r{left:531px}
  .row-1{top:54px}.row-2{top:335px}.row-3{top:616px}.row-4{top:897px}

  .backdrop{position:absolute;inset:0;width:100%;height:100%}
  .title{position:absolute;left:44px;top:22px;font-family:"Lato",sans-serif;font-size:28px;font-weight:400;color:var(--blue);letter-spacing:-.3px;white-space:nowrap}
  .title b{font-weight:900}
  .rule{position:absolute;left:0;top:66px;width:90px;height:2px;background:var(--orange)}
  .rule::after{content:"";position:absolute;right:-10px;top:-6px;width:14px;height:14px;border-radius:50%;background:var(--orange)}
  .rule.light,.rule.light::after{background:#fff}

  .footer{position:absolute;left:44px;top:387px;width:558px;height:28px;border-radius:14px;background:var(--ink);color:#fff;font-size:8px;font-weight:500;line-height:28px;padding-left:15px;letter-spacing:.1px}
  .footer.light{background:#fff;color:var(--blue)}
  .footer .num{position:absolute;right:5px;top:5px;width:18px;height:18px;border-radius:50%;background:#fff;color:var(--blue);font-size:7px;line-height:18px;text-align:center}
  .footer.light .num{background:var(--orange);color:#fff}
  .mark{position:absolute;left:632px;top:390px;font-family:"Lato",sans-serif;font-weight:900;font-size:13px;color:var(--orange);white-space:nowrap}
  .mark.light{color:#fff}

  .photo{position:absolute}

  /* cover */
  .cover{background:#000}
  .brand{position:absolute;left:44px;top:20px;font-family:"Lato",sans-serif;font-weight:700;font-size:32px;color:#fff}
  .cover-head{position:absolute;left:44px;top:138px;font-family:"Lato",sans-serif;color:#fff;font-size:28px;line-height:38px}
  .cover-head b{font-weight:900}
  .cover .rule{top:222px}
  .cover-sub{position:absolute;left:44px;top:240px;font-size:16px;line-height:23px;color:#fff;width:300px}

  /* problem */
  .bullets{position:absolute;left:44px;top:96px;width:676px;list-style:none}
  .bullets li{position:relative;padding-left:26px;font-size:10.5px;line-height:17.5px;text-align:justify;margin-bottom:12px}
  .bullets li::before{content:"";position:absolute;left:0;top:3px;width:10px;height:10px;border-radius:50%;background:var(--orange)}
  .bullets li::after{content:"";position:absolute;left:3px;top:6px;width:3px;height:3px;border-top:1.3px solid #fff;border-right:1.3px solid #fff;transform:rotate(45deg)}

  /* two columns */
  .columns{position:absolute;left:44px;top:92px;width:678px;display:grid;grid-template-columns:1fr 1fr;column-gap:32px}
  .columns p{font-size:10.5px;line-height:17.5px;text-align:justify;margin-bottom:10px}

  /* solutions */
  .solutions{background:var(--orange)}
  .solutions .title{color:#fff}
  .takeaway{position:absolute;left:90px;top:91px;width:586px;text-align:center;color:#fff;font-size:8px;line-height:14px}
  .takeaway b{font-weight:700}
  .cards{position:absolute;left:44px;top:138px;display:flex;gap:24px}
  .card{width:210px;height:222px;background:#fff;border:2px solid var(--blue);border-radius:10px;padding:18px 16px 0;text-align:center;position:relative}
  .card-name{height:40px;font-family:"Lato",sans-serif;font-weight:900;font-size:17px;color:var(--slate);line-height:40px;margin-bottom:14px}
  .card p{font-size:7.6px;line-height:13.5px;color:#333}
  .card .value{position:absolute;left:0;right:0;bottom:18px;font-size:7.6px;font-weight:700;color:var(--blue)}

  /* section */
  .section{background:var(--blue)}
  .section-title{position:absolute;left:0;right:0;top:160px;text-align:center;font-family:"Lato",sans-serif;font-size:46px;color:#fff;letter-spacing:-.5px}
  .section-title b{font-weight:900}

  /* demo */
  .demo-copy{position:absolute;left:430px;top:92px;width:292px}
  .demo-copy p{font-size:10.5px;line-height:17.5px;text-align:justify;margin-bottom:10px}

  /* insight */
  .insight-sub{position:absolute;left:44px;top:128px;width:260px;font-size:18px;line-height:23px;font-weight:500;color:var(--blue)}
  .insight-copy{position:absolute;left:44px;top:197px;width:298px;font-size:10.5px;line-height:17.5px;text-align:justify}

  /* timeline */
  .timeline{position:absolute;left:0;top:0;width:765px;height:430px}
  .tl-label{font-family:"Roboto",sans-serif;font-weight:700;font-size:8.5px;fill:var(--ink)}
  .tl-item{font-family:"Roboto",sans-serif;font-size:5.6px;fill:#444}
  .tl-q{font-family:"Roboto",sans-serif;font-size:8.5px;font-weight:500;fill:#fff}
</style>
</head>
<body>
<main class="board">

  <!-- 01 cover -->
  <section class="slide cover col-l row-1">
    <svg class="photo" width="765" height="430" viewBox="0 0 765 430" role="img" aria-label="Photo of business people meeting around a table, framed in a large round crop with a smaller round photo of a smiling woman shaking hands">
      <defs>
        <linearGradient id="g-meet" x1="0" y1="0" x2="1" y2="1">
          <stop offset="0" stop-color="#e7ecef"/><stop offset=".6" stop-color="#9aa6b0"/><stop offset="1" stop-color="#4b5560"/>
        </linearGradient>
        <linearGradient id="g-hand" x1="0" y1="0" x2="1" y2="1">
          <stop offset="0" stop-color="#d9e2e8"/><stop offset="1" stop-color="#6f7f8c"/>
        </linearGradient>
      </defs>
      <circle cx="640" cy="110" r="262" fill="url(#g-meet)" stroke="#fff" stroke-width="10"/>
      <circle cx="443" cy="268" r="78" fill="url(#g-hand)" stroke="#fff" stroke-width="10"/>
    </svg>
    <div class="brand">Ladle &amp; Lore</div>
    <h1 class="cover-head"><b>COOK, LEARN.</b><br>REPEAT</h1>
    <div class="rule"></div>
    <p class="cover-sub">Investor Overview | This document exists for our future partners.</p>
    <div class="footer light">PROPRIETARY AND CONFIDENTIAL<span class="num">01</span></div>
  </section>

  <!-- 05 problem -->
  <section class="slide col-r row-1">
    <svg class="backdrop" viewBox="0 0 765 430" aria-hidden="true"><path d="M520 0 C700 120 640 260 765 330" fill="none" stroke="#ececec" stroke-width="1.5"/><path d="M560 0 C720 140 660 280 765 360" fill="none" stroke="#f0f0ee" stroke-width="1.5"/></svg>
    <h2 class="title"><b>THE</b> PROBLEM</h2>
    <div class="rule"></div>
    <ul class="bullets">
      <li>Lorem ipsum dolor sit amet, consectetur adipiscing elit, sed do eiusmod tempor incididunt ut labore et dolore magna aliqua. Ut enim ad minim veniam, quis nostrud exercitation ullamco laboris nisi ut aliquip ex ea commodo consequat. Duis aute irure dolor in reprehenderit in voluptate velit esse cillum dolore eu fugiat nulla pariatur. Excepteur sint occaecat cupidatat non proident, sunt in culpa qui officia deserunt mollit anim id est laborum.</li>
      <li>Lorem ipsum dolor sit amet, consectetur adipiscing elit, sed do eiusmod tempor incididunt ut labore et dolore magna aliqua. Ut enim ad minim veniam, quis nostrud exercitation ullamco laboris.</li>
      <li>Lorem ipsum dolor sit amet, consectetur adipiscing elit, sed do eiusmod tempor incididunt ut labore et dolore magna aliqua. Ut enim ad minim veniam, quis nostrud exercitation ullamco laboris nisi ut aliquip ex ea commodo consequat. Duis aute irure dolor in reprehenderit in voluptate velit esse cillum dolore eu fugiat nulla pariatur.</li>
      <li>Lorem ipsum dolor sit amet, consectetur adipiscing elit, sed do eiusmod tempor incididunt ut labore et dolore magna aliqua. Ut enim ad minim veniam, quis nostrud exercitation ullamco laboris nisi ut aliquip ex ea commodo consequat. Duis aute irure dolor in reprehenderit in voluptate velit esse cillum dolore eu fugiat nulla pariatur. Excepteur sint occaecat cupidatat non proident, sunt in culpa qui officia deserunt mollit anim id est laborum.</li>
    </ul>
    <div class="footer">PROPRIETARY AND CONFIDENTIAL<span class="num">05</span></div>
    <div class="mark">Ladle &amp; Lore</div>
  </section>

  <!-- 02 what is -->
  <section class="slide col-l row-2">
    <svg class="backdrop" viewBox="0 0 765 430" aria-hidden="true"><path d="M560 0 C760 140 640 300 765 380" fill="none" stroke="#ececec" stroke-width="1.5"/></svg>
    <h2 class="title"><b>WHAT IS</b> LADLE &amp; LORE?</h2>
    <div class="rule"></div>
    <div class="columns">
      <div>
        <p>Lorem ipsum dolor sit amet, consectetur adipiscing elit, sed do eiusmod tempor incididunt ut labore et dolore magna aliqua. Ut enim ad minim veniam, quis nostrud exercitation ullamco laboris nisi ut aliquip ex ea commodo consequat. Duis aute irure dolor in reprehenderit in voluptate velit esse cillum dolore eu fugiat nulla pariatur. Excepteur sint occaecat cupidatat non proident, sunt in culpa qui officia deserunt mollit anim id est laborum.</p>
        <p>Lorem ipsum dolor sit amet, consectetur adipiscing elit, sed do eiusmod tempor incididunt ut labore et dolore magna aliqua. Ut enim ad minim veniam.</p>
        <p>Lorem ipsum dolor sit amet, consectetur adipiscing elit, sed do eiusmod tempor incididunt ut labore et dolore magna aliqua. Ut enim ad minim veniam, quis nostrud exercitation ullamco laboris nisi ut aliquip ex ea commodo consequat.</p>
      </div>
      <div>
        <p>Lorem ipsum dolor sit amet, consectetur adipiscing elit, sed do eiusmod tempor incididunt ut labore et dolore magna aliqua. Ut enim ad minim veniam, quis nostrud exercitation ullamco laboris nisi ut aliquip ex ea commodo consequat. Duis aute irure dolor in reprehenderit in voluptate velit esse cillum dolore eu fugiat nulla pariatur. Excepteur sint occaecat cupidatat non proident, sunt in culpa qui officia deserunt mollit anim id est laborum.</p>
        <p>Lorem ipsum dolor sit amet, consectetur adipiscing elit, sed do eiusmod tempor incididunt ut labore et dolore magna aliqua. Ut enim ad minim veniam.</p>
        <p>Lorem ipsum dolor sit amet, consectetur adipiscing elit, sed do eiusmod tempor incididunt ut labore et dolore magna aliqua. Ut enim ad minim veniam, quis nostrud exercitation ullamco laboris nisi ut aliquip ex ea commodo consequat.</p>
      </div>
    </div>
    <div class="footer">PROPRIETARY AND CONFIDENTIAL<span class="num">02</span></div>
    <div class="mark">Ladle &amp; Lore</div>
  </section>

  <!-- 06 current solutions -->
  <section class="slide solutions col-r row-2">
    <svg class="backdrop" viewBox="0 0 765 430" role="img" aria-label="Faint photo of a smiling person washed in orange">
      <defs><radialGradient id="g-sol" cx=".45" cy=".3" r=".8"><stop offset="0" stop-color="#ff6a3a"/><stop offset="1" stop-color="#ff3800"/></radialGradient></defs>
      <rect width="765" height="430" fill="url(#g-sol)"/>
    </svg>
    <h2 class="title"><b>CURRENT</b> SOLUTIONS</h2>
    <div class="rule light"></div>
    <p class="takeaway"><b>KEY TAKEAWAY:</b> Lorem ipsum dolor eset Lorem ipsum dolor eset Lorem ipsum dolor eset Lorem ipsum dolor eset Lorem ipsum dolor eset Lorem ipsum dolor eset Lorem ipsum dolor eset Lorem ipsum.</p>
    <div class="cards">
      <article class="card">
        <div class="card-name">Maestrova</div>
        <p>Maestrova, a leader in online prerecorded learning, offers celebrity-taught video courses across various subjects. Their high production value and renowned instructors have made them a powerhouse in the premium learning space. This success reflects the vibrancy of the online education market.</p>
        <div class="value">ESTIMATED VALUATION: $2.7B</div>
      </article>
      <article class="card">
        <div class="card-name">Table Rondelle</div>
        <p>Table Rondelle was a prominent player in the high-end kitchenware and cooking class space. They offered in-store shopping experiences with premium cookware and ingredients, alongside engaging cooking classes led by culinary professionals.</p>
        <div class="value">ESTIMATED VALUATION: $50M</div>
      </article>
      <article class="card">
        <div class="card-name">Hearthly</div>
        <p>Hearthly, another player in the online culinary education space, provides in-person and online cooking classes with a focus on connecting users with local chefs. They offer a variety of class formats, from group courses to private chef experiences</p>
        <div class="value">ESTIMATED VALUATION: $2.6M</div>
      </article>
    </div>
    <div class="footer light">PROPRIETARY AND CONFIDENTIAL<span class="num">06</span></div>
    <div class="mark light">Ladle &amp; Lore</div>
  </section>

  <!-- 03 section -->
  <section class="slide section col-l row-3">
    <svg class="backdrop" viewBox="0 0 765 430" role="img" aria-label="Photo of a group of people in conversation, tinted deep blue">
      <defs><linearGradient id="g-sec" x1="0" y1="0" x2="1" y2="1"><stop offset="0" stop-color="#0f5fa8"/><stop offset=".5" stop-color="#0b6cc3"/><stop offset="1" stop-color="#0a4f92"/></linearGradient></defs>
      <rect width="765" height="430" fill="url(#g-sec)"/>
    </svg>
    <h2 class="section-title"><b>CONSUMER</b> INSIGHTS</h2>
    <div class="footer light">PROPRIETARY AND CONFIDENTIAL<span class="num">03</span></div>
    <div class="mark light">Ladle &amp; Lore</div>
  </section>

  <!-- 07 demo -->
  <section class="slide col-r row-3">
    <svg class="backdrop" viewBox="0 0 765 430" aria-hidden="true"><path d="M560 0 C760 140 640 300 765 380" fill="none" stroke="#ececec" stroke-width="1.5"/></svg>
    <h2 class="title"><b>OUR</b> DEMO</h2>
    <div class="rule"></div>
    <svg class="photo" style="left:44px;top:92px" width="339" height="263" viewBox="0 0 339 263" role="img" aria-label="Photo of a hand holding a phone showing the Ladle &amp; Lore app in a cafe">
      <defs><linearGradient id="g-demo" x1="0" y1="0" x2="1" y2="1"><stop offset="0" stop-color="#8a5a3c"/><stop offset=".5" stop-color="#c49a78"/><stop offset="1" stop-color="#5a3a28"/></linearGradient></defs>
      <rect width="339" height="263" fill="url(#g-demo)"/>
    </svg>
    <div class="demo-copy">
      <p>Lorem ipsum dolor sit amet, consectetur adipiscing elit, sed do eiusmod tempor incididunt ut labore et dolore magna aliqua. Ut enim ad minim veniam, quis nostrud exercitation ullamco laboris nisi ut aliquip ex ea commodo consequat. Duis aute irure dolor in reprehenderit in voluptate velit esse cillum dolore eu fugiat nulla pariatur.</p>
      <p>Lorem ipsum dolor sit amet, consectetur adipiscing elit, sed do eiusmod tempor incididunt ut labore et dolore magna aliqua. Ut enim ad minim veniam.</p>
      <p>Lorem ipsum dolor sit amet, consectetur adipiscing elit, sed do eiusmod tempor incididunt ut labore et dolore magna aliqua. Ut enim ad minim veniam, quis nostrud exercitation ullamco laboris nisi ut aliquip.</p>
    </div>
    <div class="footer">PROPRIETARY AND CONFIDENTIAL<span class="num">07</span></div>
    <div class="mark">Ladle &amp; Lore</div>
  </section>

  <!-- 04 insight -->
  <section class="slide col-l row-4">
    <svg class="backdrop" viewBox="0 0 765 430" aria-hidden="true"><path d="M560 0 C760 140 640 300 765 380" fill="none" stroke="#ececec" stroke-width="1.5"/></svg>
    <h2 class="title"><b>INSIGHT</b> 1</h2>
    <div class="rule"></div>
    <h3 class="insight-sub">Growing Interest in Virtual Cooking Classes</h3>
    <p class="insight-copy">Consumers seeking alternatives, more choices, easier preference management, or simply a way to avoid crowded spaces are increasingly turning to online culinary education platforms. This trend is fueled by the desire to learn new cooking skills, explore different cuisines, and enjoy cooking as a leisure activity or a bonding experience with friends and family, even if remotely</p>
    <svg class="photo" style="left:383px;top:92px" width="339" height="263" viewBox="0 0 339 263" role="img" aria-label="Overhead photo of colleagues working together at a wooden table with laptops and coffee">
      <defs><linearGradient id="g-ins" x1="0" y1="0" x2="1" y2="1"><stop offset="0" stop-color="#cfc8bf"/><stop offset=".5" stop-color="#9a7a5c"/><stop offset="1" stop-color="#4a4a4e"/></linearGradient></defs>
      <rect width="339" height="263" fill="url(#g-ins)"/>
    </svg>
    <div class="footer">PROPRIETARY AND CONFIDENTIAL<span class="num">04</span></div>
    <div class="mark">Ladle &amp; Lore</div>
  </section>

  <!-- 08 timeline -->
  <section class="slide col-r row-4">
    <svg class="backdrop" viewBox="0 0 765 430" aria-hidden="true"><path d="M560 0 C760 140 640 300 765 380" fill="none" stroke="#ececec" stroke-width="1.5"/></svg>
    <h2 class="title"><b>PROJECT</b> TIMELINE - 2024</h2>
    <div class="rule"></div>
    <svg class="timeline" viewBox="0 0 765 430">
      <g fill="none" stroke="#2d8fdc" stroke-width=".8" stroke-dasharray="3 2">
        <path d="M186 93 H128 V200 H190 V220"/>
        <path d="M443 93 H385 V200 H448 V220"/>
        <path d="M319 247 V265 H255 V374 H314"/>
        <path d="M576 247 V265 H514 V374 H572"/>
      </g>
      <g fill="#fff" stroke="#2d8fdc" stroke-width="1.5">
        <circle cx="186" cy="93" r="3.5"/><circle cx="443" cy="93" r="3.5"/>
        <circle cx="314" cy="374" r="3.5"/><circle cx="572" cy="374" r="3.5"/>
      </g>
      <g>
        <polygon points="128,220 243,220 251,233.5 243,247 128,247 136,233.5" fill="#5bb0ee"/>
        <polygon points="255,220 373,220 381,233.5 373,247 255,247 263,233.5" fill="#2d8fdc"/>
        <polygon points="385,220 502,220 510,233.5 502,247 385,247 393,233.5" fill="#1466b8"/>
        <polygon points="514,220 631,220 639,233.5 631,247 514,247 522,233.5" fill="#0d4f8f"/>
        <text class="tl-q" x="191" y="236.5" text-anchor="middle">Q1(COMPLETE)</text>
        <text class="tl-q" x="320" y="236.5" text-anchor="middle">Q2 (COMPLETE)</text>
        <text class="tl-q" x="449" y="236.5" text-anchor="middle">Q3 (CURRENT)</text>
        <text class="tl-q" x="578" y="236.5" text-anchor="middle">Q3 (CURRENT)</text>
      </g>
      <g stroke="#2d8fdc" stroke-width=".8"><line x1="319" y1="200" x2="319" y2="220"/><line x1="576" y1="200" x2="576" y2="220"/><line x1="191" y1="247" x2="191" y2="268"/><line x1="448" y1="247" x2="448" y2="268"/></g>
      <g fill="#fff" stroke="#e8e8e8" stroke-width="1">
        <circle cx="319" cy="180" r="20"/><circle cx="576" cy="180" r="20"/>
        <circle cx="191" cy="288" r="20"/><circle cx="448" cy="288" r="20"/>
      </g>
      <g fill="none" stroke="#ff3800" stroke-width="1.2">
        <rect x="311" y="173" width="16" height="12" rx="1"/><path d="M315 189 L319 185 L323 189"/>
        <circle cx="576" cy="180" r="7"/><path d="M573 180 L576 177 L579 180 M576 177 V185"/>
        <circle cx="191" cy="285" r="6"/><path d="M188 293 H194"/>
        <circle cx="448" cy="288" r="4"/><path d="M448 280 V282 M448 294 V296 M440 288 H442 M454 288 H456"/>
      </g>
      <text class="tl-label" x="319" y="126" text-anchor="middle">DESIGN REFINEMENT &amp;</text>
      <text class="tl-label" x="319" y="138" text-anchor="middle">PROTOTYPING</text>
      <text class="tl-label" x="576" y="130" text-anchor="middle">LAUNCH &amp; POST-LAUNCH</text>
      <text class="tl-label" x="576" y="142" text-anchor="middle">ACTIVITIES</text>
      <text class="tl-label" x="191" y="326" text-anchor="middle">IDEATION &amp; DESIGN</text>
      <text class="tl-label" x="448" y="326" text-anchor="middle">DEVELOPMENT &amp;</text>
      <text class="tl-label" x="448" y="338" text-anchor="middle">PRE-MARKETING</text>
      <g fill="#2d8fdc">
        <circle cx="140" cy="113" r="2"/><circle cx="140" cy="139" r="2"/><circle cx="140" cy="165" r="2"/>
        <circle cx="267" cy="283" r="2"/><circle cx="267" cy="309" r="2"/><circle cx="267" cy="335" r="2"/>
      </g>
      <g fill="#0d4f8f">
        <circle cx="395" cy="112" r="2"/><circle cx="395" cy="122" r="2"/><circle cx="395" cy="132" r="2"/><circle cx="395" cy="152" r="2"/><circle cx="395" cy="162" r="2"/><circle cx="395" cy="182" r="2"/>
        <circle cx="524" cy="278" r="2"/><circle cx="524" cy="294" r="2"/><circle cx="524" cy="306" r="2"/><circle cx="524" cy="318" r="2"/><circle cx="524" cy="331" r="2"/>
      </g>
      <g class="tl-item">
        <text x="146" y="115">Brainstorming and defining</text><text x="146" y="123">project concept</text>
        <text x="146" y="141">User research and target</text><text x="146" y="149">audience identification</text>
        <text x="146" y="167">Developing project</text><text x="146" y="175">requirements and specifications</text>

        <text x="401" y="114">Source Pre-seed Funding</text>
        <text x="401" y="124">Front-end &amp; back-end development</text>
        <text x="401" y="134">Integration of functionalities based</text><text x="401" y="141">on design</text>
        <text x="401" y="154">Testing and bug fixing</text>
        <text x="401" y="164">Preparing marketing materials (e.g.,</text><text x="401" y="171">website copy, social media content)</text>
        <text x="401" y="184">Identifying target marketing channels</text>

        <text x="273" y="285">Design Refinement &amp;</text><text x="273" y="293">Prototyping</text>
        <text x="273" y="311">Refining and finalizing user</text><text x="273" y="319">interface (UI) &amp; user experience</text>
        <text x="273" y="337">Developing a style guide for</text><text x="273" y="345">consistent branding</text>

        <text x="530" y="280">Final product testing and quality</text><text x="530" y="287">assurance (QA)</text>
        <text x="530" y="296">Product launch (target: Early November)</text>
        <text x="530" y="308">Initial marketing campaign execution</text>
        <text x="530" y="320">User acquisition and onboarding</text>
        <text x="530" y="333">Gathering user feedback and</text><text x="530" y="340">iteration based on post-launch data</text>
      </g>
    </svg>
    <div class="footer">PROPRIETARY AND CONFIDENTIAL<span class="num">08</span></div>
    <div class="mark">Ladle &amp; Lore</div>
  </section>

</main>
</body>
</html>
```